Business Card Design needed for logo design project

This project is linked to a href='http://jobs.pixelfennel.example/job.aspx?id=412907'Tide Nook: Design a logo for our new trailer boat syndication business in Sydney
Our company needs a Business Card Design. Please refer to our original project in the link above.
I would like a relatively simple and classy business card design. could you please also use small symbols for identifying contact info eg. mobile, web and email?
Updates
Please see my new project to design a business card for a trailer boat syndication business in Sydney, Australia.
Industry/Entity Type
Business
Look and feel
Each slider illustrates characteristics of the customer's brand and the style your logo design should communicate.

```html
<!DOCTYPE html>
<html lang="en">
<head>
<meta charset="utf-8">
<title>Tide Nook business card</title>
<link rel="stylesheet" href="https://fonts.googleapis.com/css2?family=Exo+2:ital,wght@0,400;0,600;0,800;1,400;1,600&display=swap">
<style>
  :root {
    --teal: #3faab5;
    --grey: #6f6f71;
    --ink: #1d1a1f;
    --paper: #ffffff;
    --stage: #e4e4e4;
    --text: #5b5b5d;
  }
  * { box-sizing: border-box; margin: 0; padding: 0; }
  html, body { width: 1200px; height: 900px; overflow: hidden; }
  body {
    background: var(--stage);
    font-family: "Exo 2", sans-serif;
    position: relative;
  }
  .card {
    position: absolute;
    top: 302px;
    width: 515px;
    height: 296px;
    overflow: hidden;
    box-shadow: 0 4px 12px rgba(0,0,0,.25);
  }
  .card-front { left: 72px; background: var(--ink); }
  .card-back { left: 615px; background: var(--paper); }

  .brand-name {
    position: absolute;
    font-weight: 800;
    color: var(--teal);
    letter-spacing: -0.5px;
    line-height: 1;
  }
  .brand-tagline {
    position: absolute;
    font-weight: 600;
    font-size: 7px;
    letter-spacing: 0.6px;
    text-transform: uppercase;
    white-space: nowrap;
  }
  .card-front .brand-name { left: 68px; top: 132px; font-size: 42px; }
  .card-front .brand-tagline { left: 69px; top: 176px; color: #d8d8d8; }

  .card-back .brand-mark {
    position: absolute;
    left: 150px; top: 62px;
    width: 14px; height: 14px;
    border-radius: 50%;
    background: var(--teal);
  }
  .card-back .brand-name { left: 173px; top: 52px; font-size: 40px; }
  .card-back .brand-tagline { left: 175px; top: 92px; color: var(--ink); }

  .person { position: absolute; left: 48px; top: 150px; font-style: italic; font-size: 15px; line-height: 20px; }
  .person-name { color: var(--teal); font-weight: 600; }
  .person-role { color: var(--text); font-weight: 600; }

  .contact-list { position: absolute; top: 208px; list-style: none; font-style: italic; font-size: 13.5px; line-height: 18px; color: var(--text); }
  .contact-direct { left: 48px; }
  .contact-direct li { display: flex; align-items: center; gap: 8px; }
  .contact-direct svg { width: 10px; height: 10px; fill: var(--teal); flex: none; }
  .contact-place { left: 310px; }
  .contact-place .web { color: var(--teal); }

  .card-bands { position: absolute; left: 0; bottom: 0; width: 515px; height: 26px; }
</style>
</head>
<body>

<section class="card card-front" aria-label="Card front">
  <div class="brand-name">Tide Nook</div>
  <div class="brand-tagline">Trailer boat syndication and management</div>
</section>

<section class="card card-back" aria-label="Card back">
  <span class="brand-mark"></span>
  <div class="brand-name">Tide Nook</div>
  <div class="brand-tagline">Trailer boat syndication and management</div>

  <div class="person">
    <div class="person-name">Owen Marlow</div>
    <div class="person-role">managing director</div>
  </div>

  <ul class="contact-list contact-direct">
    <li><svg viewBox="0 0 10 10"><path d="M2 0.5 L3.6 2.6 L2.7 3.7 Q3.6 5.6 5.9 7 L7 6.1 L9.5 7.6 L8.4 9.5 Q3.5 8.8 0.5 2 Z"/></svg>555 555 55 55</li>
    <li><svg viewBox="0 0 10 10"><path d="M2.5 0 H7.5 V10 H2.5 Z M3.4 1 V8 H6.6 V1 Z"/></svg>888 888 88 88</li>
    <li><svg viewBox="0 0 10 10"><path d="M0 2 H10 V8.5 H0 Z M0.8 2.6 L5 5.6 L9.2 2.6 Z"/></svg>omarlow@tidenook.com.au</li>
  </ul>

  <ul class="contact-list contact-place">
    <li>48 Harbour Lane</li>
    <li>Bayview, NSW, 2104</li>
    <li class="web">www.tidenook.com.au</li>
  </ul>

  <svg class="card-bands" viewBox="0 0 515 26" aria-hidden="true">
    <polygon points="0,0 298,0 274,26 0,26" fill="var(--teal)"/>
    <polygon points="311,0 515,0 515,26 287,26" fill="var(--grey)"/>
  </svg>
</section>

</body>
</html>
```